Driving-coach/trainer who wants to inform about the offer and how I can help people to drive more re

I need a flyer that informs potential customers about my offer.

DL size 210 mm x 99 mm, vertical!

I'm a trainer/coach who helps people to drive a car more relaxed, without fear and more confident.

It's a one to one training. I do train people in their own car. It gets people their freedom back to go where and when they like to go by own car...

Target Market(s)

People (man an woman) who are afraid of driving a car, or are very stressed while driving....

Industry/Entity Type

Life Coaching

Font styles to use
Sans Serif

Colors
acd136

Requirements
Must have
• Page 1:
• -my offer (see text-pdf)
• -three fotos (see attached files "Pixmarra") of people who are satisfied with my offer
• Page 2:
• -advantages in the work with me.
• -contact information
• -and a picture of me (see attached file) next to the contact information or the advantages of my work
• -my logo (see attached file) on Page 1 + 2
• -i like a "clear" and structured layout. "Less is more"

```html
<!DOCTYPE html>
<html lang="de">
<head>
<meta charset="utf-8">
<title>Fahrangst-Bewältigungs-Coach – Flyer</title>
<link href="https://fonts.googleapis.com/css2?family=Open+Sans:wght@400;600;700;800&display=swap" rel="stylesheet">
<style>
  :root {
    --green: #8cc63f;
    --green-dark: #6fa82a;
    --green-light: #acd136;
    --gray-dark: #4a4a4a;
    --gray-mid: #6b6b6b;
    --white: #ffffff;
    --ink: #111111;
  }
  * { margin: 0; padding: 0; box-sizing: border-box; }
  html, body { width: 1200px; height: 2776px; overflow: hidden; background: var(--white); }
  body { font-family: "Open Sans", Arial, sans-serif; }
  .flyer { position: relative; width: 1200px; height: 2776px; overflow: hidden; background: var(--white); }

  .hero-photo {
    position: absolute; left: 0; top: 380px; width: 1200px; height: 840px;
    background: linear-gradient(160deg, #dfe6d8 0%, #b9c6a6 30%, #8f9a86 55%, #cfd3d6 80%, #eef0f2 100%);
  }
  .header-shape { position: absolute; left: 0; top: 0; width: 1200px; height: 520px; }

  .header-title {
    position: absolute; left: 40px; top: 18px;
    font-size: 104px; font-weight: 400; color: var(--white); letter-spacing: -1px;
  }
  .header-list { position: absolute; left: 40px; top: 150px; list-style: none; }
  .header-list li {
    position: relative; padding-left: 70px; height: 88px;
    font-size: 44px; font-weight: 600; color: var(--white); line-height: 88px;
  }
  .tri {
    position: absolute; left: 0; width: 0; height: 0;
    border-left: 28px solid transparent; border-bottom: 28px solid var(--white);
  }
  .header-list .tri { top: 30px; }

  .hero-claim {
    position: absolute; left: 60px; top: 500px;
    font-size: 60px; font-weight: 800; color: var(--ink); line-height: 1.2;
  }

  .situations {
    position: absolute; left: 0; top: 1200px; width: 1200px; height: 1192px;
    background: linear-gradient(180deg, var(--gray-mid) 0%, var(--gray-dark) 100%);
    padding: 40px 60px 0 80px; color: var(--white);
  }
  .situations h2 { font-size: 52px; font-weight: 700; line-height: 1.2; margin-bottom: 34px; }
  .situation { position: relative; padding-left: 56px; margin-bottom: 34px; }
  .situation:last-child { margin-bottom: 0; }
  .situation .tri { top: 12px; border-left-width: 24px; border-bottom-width: 24px; }
  .situation p { font-size: 41px; line-height: 53px; font-weight: 400; }
  .situation .wish { font-size: 40px; font-weight: 700; margin-top: 6px; }

  .solution-band {
    position: absolute; left: 0; top: 2392px; width: 1200px; height: 210px;
    background: var(--green); color: var(--white);
  }
  .solution-band .lead { position: absolute; left: 40px; top: 22px; font-size: 50px; font-weight: 400; }
  .solution-band .steps { position: absolute; left: 40px; top: 92px; font-size: 74px; font-weight: 800; letter-spacing: 1px; }
  .chevrons { position: absolute; right: 0; top: 0; width: 360px; height: 210px; }

  .signature { position: absolute; left: 60px; top: 2616px; color: var(--green-dark); }
  .signature .name { font-size: 62px; font-weight: 400; letter-spacing: 2px; }
  .signature .role { font-size: 40px; font-weight: 400; letter-spacing: 3px; margin-top: -4px; }
</style>
</head>
<body>
<div class="flyer">

  <div class="hero-photo" role="img" aria-label="Foto: lächelnde Frau lehnt aus dem Fenster eines weißen Autos und zeigt den Daumen nach oben"></div>

  <svg class="header-shape" viewBox="0 0 1200 520" aria-hidden="true">
    <polygon points="0,0 1200,0 1200,400 0,480" fill="#ffffff"/>
    <polygon points="0,0 1200,0 1200,372 0,452" fill="var(--green)"/>
    <polygon points="0,452 1200,372 1200,400 0,480" fill="#ffffff"/>
    <polygon points="0,480 1200,400 1200,420 0,500" fill="var(--green-light)" opacity="0.6"/>
  </svg>

  <h1 class="header-title">Wollen Sie</h1>
  <ul class="header-list">
    <li><span class="tri"></span>Fahrangst überwinden?</li>
    <li><span class="tri"></span>Panikattacken beim Autofahren loswerden?</li>
    <li><span class="tri"></span>Oder einfach sicher Autofahren?</li>
  </ul>

  <p class="hero-claim">Dann sind<br>Sie hier richtig!</p>

  <section class="situations">
    <h2>Kommt Ihnen eine<br>dieser Situationen bekannt vor?</h2>

    <div class="situation">
      <span class="tri"></span>
      <p>Angst oder Panikattacken begleiten Sie beim<br>Autofahren. Vielleicht vermeiden Sie deshalb das<br>Autofahren komplett.</p>
      <p class="wish">- Sie möchten angstfrei und/oder ohne<br>Panikattacken fahren.</p>
    </div>

    <div class="situation">
      <span class="tri"></span>
      <p>Sie trauen sich das Autofahren nicht (mehr) zu.</p>
      <p class="wish">- Sie wünschen sich, sicher, entspannt und<br>stressfrei Auto zu fahren.</p>
    </div>

    <div class="situation">
      <span class="tri"></span>
      <p>Autofahren erleben Sie unter hoher Anspannung<br>und Stress.</p>
      <p class="wish">- Sie wünschen sich, Autofahren sicher und<br>entspannt zu erleben.</p>
    </div>

    <div class="situation">
      <span class="tri"></span>
      <p>Bestimmte Situationen (z.B. Autobahn, Baustellen,<br>Stadtvekehr...) bereiten Ihnen großen Stress.</p>
      <p class="wish">- Sie möchten diese Situationen souveräner<br>meistern.</p>
    </div>
  </section>

  <div class="solution-band">
    <p class="lead">Das muss nicht so bleiben!</p>
    <p class="steps">3 Schritte zur Lösung:</p>
    <svg class="chevrons" viewBox="0 0 360 210" aria-hidden="true">
      <polygon points="40,0 130,0 220,105 130,210 40,210 130,105" fill="var(--green-dark)" opacity="0.55"/>
      <polygon points="170,0 260,0 350,105 260,210 170,210 260,105" fill="var(--green-dark)" opacity="0.8"/>
    </svg>
  </div>

  <div class="signature">
    <p class="name">Karin Wendelberg</p>
    <p class="role">Fahrangst-Bewältigungs-Coach</p>
  </div>

</div>
</body>
</html>
```